Saltmarsh Valley Lending Flyer

I would like our main long logo with the bird and words Saltmarsh Valley Lending with pictures of what we finance along the bottom.
Car , 4x4 , boat, excavator , Cash Loans and houses
Needs to look good on leaflet and large signage.
Simple but cool looking so it stands out.

```html
<!DOCTYPE html>
<html lang="en">
<head>
<meta charset="utf-8">
<title>Saltmarsh Valley Lending Flyer</title>
<link href="https://fonts.googleapis.com/css2?family=Cinzel:wght@400;600&family=Crimson+Text:wght@700&display=swap" rel="stylesheet">
<style>
  :root {
    --backdrop: #878787;
    --paper: #ffffff;
    --accent: #ec6a12;
    --ink: #1c1c1c;
    --footer: #3d3a38;
    --band: rgba(40, 70, 20, 0.55);
    --leaf-light: #b7d48a;
    --leaf-mid: #5f9a3a;
    --leaf-dark: #2f5a22;
  }
  * { box-sizing: border-box; margin: 0; padding: 0; }
  html, body { width: 1200px; height: 1200px; overflow: hidden; }
  body { background: var(--backdrop); position: relative; font-family: "Cinzel", serif; }

  .flyer {
    position: absolute; left: 291px; top: 197px;
    width: 697px; height: 901px;
    background: var(--paper); overflow: hidden;
  }
  .hero-photo {
    position: absolute; left: 0; top: 0; width: 697px; height: 460px;
    background:
      linear-gradient(180deg, rgba(255,255,255,0) 78%, #ffffff 100%),
      radial-gradient(ellipse at 50% 62%, #d9b79a 0%, #b98d74 18%, rgba(90,140,60,0) 45%),
      linear-gradient(180deg, var(--leaf-light) 0%, var(--leaf-mid) 35%, var(--leaf-dark) 60%, #86b25a 82%);
  }
  .headline-band {
    position: absolute; left: 0; top: 41px; width: 697px; height: 84px;
    background: var(--band);
    border-bottom: 1px solid rgba(255,255,255,0.25);
    text-align: center; color: #fff;
    font-size: 35px; line-height: 36px; padding-top: 7px; letter-spacing: 0.5px;
  }
  .headline-band .hl { color: var(--accent); }

  .products-frame {
    position: absolute; left: 30px; top: 477px; width: 637px; height: 174px;
    border: 2px solid var(--accent);
  }
  .products-art {
    position: absolute; left: 41px; top: 419px; width: 620px; height: 172px;
    background: linear-gradient(90deg, #d98a5a 0%, #c9c9c9 30%, #2f3a4a 45%, #e6b81c 62%, #e8eef2 75%, #c9b25a 90%, #6ea35a 100%);
    opacity: 0.85;
    border-radius: 4px;
  }
  .loans-title {
    position: absolute; left: 0; top: 593px; width: 697px; text-align: center;
    font-size: 21px; color: var(--ink);
  }
  .loans-list {
    position: absolute; left: 0; top: 622px; width: 697px; text-align: center;
    font-size: 19px; color: var(--accent); word-spacing: 1px;
  }
  .loans-list .sep { color: var(--ink); font-size: 12px; vertical-align: 3px; margin: 0 5px; }

  .brand {
    position: absolute; left: 97px; top: 688px; width: 560px; height: 110px;
  }
  .brand-mark {
    position: absolute; left: 0; top: 12px; width: 86px; height: 86px;
    background: var(--accent);
  }
  .brand-name {
    position: absolute; left: 112px; top: 6px;
    font-weight: 600; color: var(--ink); font-size: 40px; line-height: 46px;
  }

  .contact-bar {
    position: absolute; left: 0; top: 826px; width: 697px; height: 75px;
    background: var(--footer); color: #fff;
    font-family: "Crimson Text", serif; font-weight: 700; font-size: 14px;
    display: flex; align-items: flex-start; justify-content: center; gap: 18px;
    padding-top: 14px;
  }
  .contact-item { display: flex; align-items: center; gap: 7px; }
  .contact-item svg { width: 17px; height: 17px; fill: var(--accent); flex: none; }
</style>
</head>
<body>
  <main class="flyer">
    <div class="hero-photo" role="img" aria-label="Photo of a smiling family of four lying on the grass in a leafy park"></div>
    <h1 class="headline-band">
      WE <span class="hl">HELP</span> WEAR THAT <span class="hl">SMILE</span><br>ON YOUR FACE
    </h1>

    <div class="products-frame"></div>
    <div class="products-art" role="img" aria-label="Row of financed items: a house, a 4x4, a car, an excavator, a boat and rolled banknotes"></div>
    <p class="loans-title">WE PROVIDE LOANS FOR:</p>
    <p class="loans-list">CAR<span class="sep">■</span>4X4<span class="sep">■</span>BOAT<span class="sep">■</span>EXCAVATOR<span class="sep">■</span>CASH LOANS<span class="sep">■</span>HOUSES</p>

    <div class="brand">
      <div class="brand-mark"></div>
      <p class="brand-name">Saltmarsh Valley<br>Lending</p>
    </div>

    <footer class="contact-bar">
      <span class="contact-item">
        <svg viewBox="0 0 24 24"><path d="M12 2a7 7 0 0 0-7 7c0 5 7 13 7 13s7-8 7-13a7 7 0 0 0-7-7zm0 9.5A2.5 2.5 0 1 1 12 6.5a2.5 2.5 0 0 1 0 5z"/></svg>
        Unit 4, 27 Heron Street, Marshbank NT 0830
      </span>
      <span class="contact-item">
        <svg viewBox="0 0 24 24"><path d="M6.6 10.8a15 15 0 0 0 6.6 6.6l2.2-2.2a1 1 0 0 1 1-.25 11.4 11.4 0 0 0 3.6.57 1 1 0 0 1 1 1V20a1 1 0 0 1-1 1A17 17 0 0 1 3 4a1 1 0 0 1 1-1h3.5a1 1 0 0 1 1 1c0 1.25.2 2.45.57 3.57a1 1 0 0 1-.25 1z"/></svg>
        08 5550 1274
      </span>
      <span class="contact-item">
        <svg viewBox="0 0 24 24"><path d="M12 2a10 10 0 1 0 0 20 10 10 0 0 0 0-20zm0 2a8 8 0 0 1 7.7 5.8H16c-.3-1.9-.9-3.6-1.7-4.9A8 8 0 0 1 12 4zm-2.3.9C8.9 6.2 8.3 7.9 8 9.8H4.3A8 8 0 0 1 9.7 4.9zM4 12h4v2H4.3A8 8 0 0 1 4 12zm6 0h4v2h-4zm6 0h4a8 8 0 0 1-.3 2H16zM4.9 16H8c.3 1.3.8 2.4 1.5 3.3A8 8 0 0 1 4.9 16zm5.2 0h3.8c-.4 1.6-1.1 2.9-1.9 3.6-.8-.7-1.5-2-1.9-3.6zm5.9 0h3.1a8 8 0 0 1-4.6 3.3c.7-.9 1.2-2 1.5-3.3z"/></svg>
        www.saltmarshlending.com.au
      </span>
    </footer>
  </main>
</body>
</html>
```